Design some cool and useful Business Cards

The following should be on the business card of a business providing outdoor teambuilding activities:

Front:
* Website name: "waldkreisEvents.de"
* Business owner: "Klaus-Dieter Bramsch"
* Phone: "+49 162 738 204 61"
* Mail: "dieter@waldkreisevents.de"
* Slogan: "natürlich anders" (naturally different)
* Visualization of the slogan

Back:
Slogan: "Natürlich sicher" (naturally secure)
"Passwort Generator"
[password encoding fields (without the black signs), refer to sample on attached photo]

Size: 86x54 mm
Colors in CMYK
300 DPI

```html
<!DOCTYPE html>
<html lang="de">
<head>
<meta charset="utf-8">
<title>waldkreisEvents.de – Visitenkarten</title>
<link rel="stylesheet" href="https://fonts.googleapis.com/css2?family=Bebas+Neue&family=Open+Sans:wght@400;600;700&display=swap">
<style>
  :root {
    --backdrop: #d6d6d6;
    --card-green: #4bb451;
    --ink: #141414;
    --paper: #ffffff;
    --wool: #f7f1e3;
    --wool-shade: #e6dcc6;
    --muted-white: rgba(255,255,255,0.9);
  }
  * { box-sizing: border-box; margin: 0; padding: 0; }
  html, body {
    width: 1200px; height: 900px; overflow: hidden;
    background: var(--backdrop);
    font-family: "Open Sans", Arial, sans-serif;
  }
  .stage { position: relative; width: 1200px; height: 900px; }

  .card {
    position: absolute;
    width: 620px; height: 389px;
    background: var(--card-green);
    border-radius: 28px;
    overflow: hidden;
  }
  .card--back { left: 60px; top: 50px; }
  .card--front { left: 520px; top: 460px; }

  .brand {
    position: absolute;
    display: flex; align-items: center; gap: 8px;
    font-weight: 700; font-size: 15px; letter-spacing: 0.2px;
  }
  .brand__dot { width: 14px; height: 14px; border-radius: 50%; }
  .card--back .brand { left: 50%; transform: translateX(-50%); top: 52px; color: var(--paper); }
  .card--back .brand__dot { background: var(--paper); }
  .card--front .brand { left: 270px; transform: translateX(-50%); top: 100px; color: var(--ink); }
  .card--front .brand__dot { background: var(--ink); }

  .slogan {
    position: absolute;
    font-family: "Bebas Neue", "Arial Narrow", sans-serif;
    color: var(--ink);
    white-space: nowrap;
    letter-spacing: 1px;
  }
  .card--back .slogan { left: 50%; transform: translateX(-50%); top: 110px; font-size: 84px; line-height: 1; }
  .card--front .slogan { left: 270px; transform: translateX(-50%); top: 150px; font-size: 50px; line-height: 1; }

  .password-grid {
    position: absolute; left: 40px; right: 40px; top: 262px;
    display: flex; justify-content: space-between; align-items: flex-start;
  }
  .password-field { display: flex; flex-direction: column; align-items: center; gap: 6px; }
  .password-field__box { width: 46px; height: 30px; background: var(--paper); }
  .password-field--start .password-field__box { width: 78px; }
  .password-field__label { font-size: 12px; color: var(--paper); letter-spacing: 0.5px; }

  .sheep-visual {
    position: absolute; left: 478px; top: 40px;
    width: 200px; height: 170px;
    border-radius: 50%;
    background: radial-gradient(circle at 55% 50%, var(--paper) 0%, var(--wool) 55%, var(--wool-shade) 100%);
  }

  .contact { position: absolute; left: 34px; top: 268px; color: var(--paper); }
  .contact__name {
    font-family: "Bebas Neue", "Arial Narrow", sans-serif;
    font-size: 28px; line-height: 1; letter-spacing: 0.5px; text-transform: uppercase;
  }
  .contact__role { font-size: 12px; color: var(--muted-white); text-transform: uppercase; margin-top: 2px; }
  .contact__line {
    display: flex; align-items: center; gap: 10px;
    font-size: 13px; color: var(--muted-white); margin-top: 8px;
  }
  .contact__icon { width: 14px; height: 14px; flex: none; }
</style>
</head>
<body>
<main class="stage">

  <section class="card card--back" aria-label="Rückseite">
    <div class="brand"><span class="brand__dot"></span><span>waldkreisEvents.de</span></div>
    <h2 class="slogan">Natürlich sicher</h2>
    <div class="password-grid" aria-label="Passwort Generator">
      <div class="password-field password-field--start"><span class="password-field__box"></span><span class="password-field__label">START</span></div>
      <div class="password-field"><span class="password-field__box"></span><span class="password-field__label">ABC</span></div>
      <div class="password-field"><span class="password-field__box"></span><span class="password-field__label">DEF</span></div>
      <div class="password-field"><span class="password-field__box"></span><span class="password-field__label">GHI</span></div>
      <div class="password-field"><span class="password-field__box"></span><span class="password-field__label">JKL</span></div>
      <div class="password-field"><span class="password-field__box"></span><span class="password-field__label">MNO</span></div>
      <div class="password-field"><span class="password-field__box"></span><span class="password-field__label">PQRS</span></div>
      <div class="password-field"><span class="password-field__box"></span><span class="password-field__label">TUV</span></div>
      <div class="password-field"><span class="password-field__box"></span><span class="password-field__label">WXYZ</span></div>
    </div>
  </section>

  <section class="card card--front" aria-label="Vorderseite">
    <div class="brand"><span class="brand__dot"></span><span>waldkreisEvents.de</span></div>
    <h1 class="slogan">Natürlich anders</h1>
    <div class="sheep-visual" role="img" aria-label="Illustration eines lächelnden weißen Schafs, das vom rechten Kartenrand hereinschaut"></div>
    <div class="contact">
      <p class="contact__name">Klaus-Dieter Bramsch</p>
      <p class="contact__role">Owner</p>
      <p class="contact__line">
        <svg class="contact__icon" viewBox="0 0 14 14" aria-hidden="true"><rect x="3.5" y="0.8" width="7" height="12.4" rx="1.4" fill="none" stroke="#fff" stroke-width="1.2"/><circle cx="7" cy="11" r="0.8" fill="#fff"/></svg>
        <span>+49 162 738 204 61</span>
      </p>
      <p class="contact__line">
        <svg class="contact__icon" viewBox="0 0 14 14" aria-hidden="true"><rect x="0.8" y="2.8" width="12.4" height="8.4" rx="1" fill="none" stroke="#fff" stroke-width="1.2"/><path d="M1 3.4 L7 8 L13 3.4" fill="none" stroke="#fff" stroke-width="1.2"/></svg>
        <span>dieter@waldkreisevents.de</span>
      </p>
    </div>
  </section>

</main>
</body>
</html>
```